Updated web design for software design firm supporting entrepreneurs

Looking for a more modern looking, mobile friendly website design for our company, Brainwave2Binaries. B2B is a software development firm who supports people who have ideas for software and want to make them a reality. It also provides some maintenance work on existing websites as well as mobile apps. Please see our current website, www.brainwave2binaries-example.com, for more information on our business.

Old logo files included for reference. However, we are hoping to incorporate a new logo.

Like a blue'ish theme, but open to ideas.

Industry/Entity Type

Software

Logo Text

B2B and/or Brainwave2Binaries

Number of Pages Required

2 page

Font styles to use
Serif
Sans Serif

Colors
33a6d7
0255a3

Requirements
Must have
• Looking for 2 pages designed: 1 landing page and 1 type of secondary content page
• Please prepare menu for about 7 pages
Nice to have
• This will be implemented as a WordPress theme.
• Could include post-it note, white board, napkins, etc.

```html
<!DOCTYPE html>
<html lang="en">
<head>
<meta charset="utf-8">
<title>About Us – Brainwave2Binaries</title>
<link href="https://fonts.googleapis.com/css2?family=Arimo:wght@400;700&family=Montserrat:wght@700&family=Roboto+Slab:wght@400&family=Exo+2:wght@600&display=swap" rel="stylesheet">
<style>
:root{
  --navy:#0255a3;
  --sky:#33a6d7;
  --sky-soft:#7ec8e8;
  --band-dark:#5b8fc9;
  --paper:#f4f5f7;
  --line:#d9dde2;
  --text:#555a60;
  --muted:#7a7f85;
  --white:#ffffff;
  --footer:#0c3f85;
}
*{box-sizing:border-box;margin:0;padding:0}
html,body{width:806px;height:1200px;overflow:hidden}
body{position:relative;background:var(--white);font-family:"Arimo",Arial,sans-serif;color:var(--text)}
.abs{position:absolute}

.site-header{left:0;top:0;width:806px;height:71px;background:var(--white)}
.brand{left:0;width:806px;top:18px;text-align:center;font-family:"Exo 2",sans-serif;font-weight:600;font-size:30px;color:var(--navy);letter-spacing:2px}

.main-nav{left:0;top:71px;width:806px;height:41px;background:var(--navy)}
.main-nav a{position:absolute;top:0;height:41px;line-height:41px;color:var(--white);font-size:9px;font-weight:700;text-decoration:none;text-align:center}
.main-nav a.active{background:var(--sky)}

.hero{left:0;top:112px;width:806px;height:201px;background:linear-gradient(120deg,#6fa9b9 0%,#c9b85a 30%,#e6c93a 50%,#d9b94a 70%,#6aa7bd 100%)}
.hero h1{position:absolute;left:0;width:806px;top:72px;text-align:center;font-family:"Montserrat",sans-serif;font-size:35px;color:var(--white)}
.hero p{position:absolute;left:0;width:806px;top:121px;text-align:center;font-size:8px;color:var(--white)}

.about{left:0;top:313px;width:806px;height:273px;background:var(--paper)}
.about-box{left:79px;top:92px;width:648px;height:162px;border:1px solid var(--line);background:var(--white)}
.about-photo{left:102px;top:36px;width:206px;height:193px;background:var(--white);box-shadow:0 4px 6px rgba(0,0,0,.2);padding:3px}
.about-photo div{width:100%;height:100%;background:linear-gradient(135deg,#b78c74 0%,#d6b6a0 40%,#3a86c6 75%,#2a6aa8 100%)}
.about-title{left:336px;top:51px;font-family:"Exo 2",sans-serif;font-weight:600;font-size:16px;color:var(--navy);letter-spacing:.5px}
.about-title span{color:var(--sky)}
.about-rule{left:320px;top:74px;width:256px;height:1px;background:var(--line)}
.about-vrule{left:328px;top:45px;width:1px;height:28px;background:var(--line)}
.about-text{left:330px;top:108px;width:376px;font-size:7.6px;line-height:17.3px}
.about-text p+p{margin-top:11px}

.team{left:0;top:586px;width:806px;height:286px;background:var(--white)}
.arrow{top:108px}
.card{top:26px;width:162px;height:229px;background:var(--white);box-shadow:0 0 3px rgba(0,0,0,.15)}
.card .band{position:absolute;left:0;top:0;width:162px;height:54px}
.card .avatar{position:absolute;left:42px;top:17px;width:78px;height:78px;border-radius:50%;border:3px solid var(--white);background:linear-gradient(160deg,#c9b3a5,#8e7565)}
.card h3{position:absolute;left:0;width:162px;top:108px;text-align:center;font-family:"Roboto Slab",serif;font-weight:400;font-size:12.5px;color:#444}
.card .role{position:absolute;left:0;width:162px;top:127px;text-align:center;font-family:"Roboto Slab",serif;font-size:9px;color:#555}
.card .bio{position:absolute;left:14px;width:134px;top:145px;text-align:center;font-size:7.8px;line-height:14.4px;color:var(--muted)}
.card .divider{position:absolute;left:0;top:194px;width:162px;height:1px;background:#e6e8eb}
.card svg{position:absolute;left:23px;top:202px}

.contact{left:0;top:872px;width:806px;height:285px;background:var(--paper)}
.contact h2{position:absolute;left:0;width:806px;top:24px;text-align:center;font-family:"Exo 2",sans-serif;font-weight:600;font-size:15px;color:var(--navy)}
.contact h2 span{color:var(--sky)}
.contact .lead{position:absolute;left:0;width:806px;top:55px;text-align:center;font-size:7.8px}
.field{position:absolute;background:var(--white);border:1px solid var(--line);font-size:7.8px;color:var(--muted);padding:7px 7px}
.submit{position:absolute;left:58px;top:240px;width:47px;height:19px;background:var(--sky);color:var(--white);font-size:7.8px;font-weight:700;line-height:19px;text-align:center}
.info-lead{left:419px;top:86px;width:316px;font-size:7.8px;line-height:14.5px;color:#444}
.label-sm{font-size:7px;color:#444;text-transform:uppercase}
.label-lg{font-family:"Exo 2",sans-serif;font-weight:600;font-size:10.5px;color:#444;letter-spacing:.5px}
.info{font-size:7.8px;line-height:14px;color:var(--muted)}

.site-footer{left:0;top:1157px;width:806px;height:43px;background:var(--footer);color:var(--white);font-size:8px;text-align:center;line-height:43px}
</style>
</head>
<body>

<header class="abs site-header">
  <div class="abs brand">B2B</div>
</header>

<nav class="abs main-nav">
  <a style="left:71px;width:60px">HOME</a>
  <a class="active" style="left:138px;width:82px">ABOUT US</a>
  <a style="left:240px;width:80px">HOW IT WORKS</a>
  <a style="left:344px;width:80px">WHO WE ARE</a>
  <a style="left:450px;width:80px">WHO NEEDS US?</a>
  <a style="left:553px;width:80px">PORTFOLIO</a>
  <a style="left:650px;width:80px">CONTACT US</a>
</nav>

<section class="abs hero" role="img" aria-label="Wall of handwritten sticky notes in yellow and blue">
  <h1>ABOUT US</h1>
  <p>Brainwave2Binaries can help anyone turn their software idea into reality. We understand that you don't have to be a big</p>
</section>

<section class="abs about">
  <div class="abs about-box"></div>
  <div class="abs about-photo"><div role="img" aria-label="Photo of the two founders smiling on a bridge"></div></div>
  <div class="abs about-vrule"></div>
  <h2 class="abs about-title">ABOUT <span>BRAINWAVE2BINARIES</span></h2>
  <div class="abs about-rule"></div>
  <div class="abs about-text">
    <p>Brainwave2Binaries can help anyone turn their software idea into reality. We understand that you don't have to be a big company to have big ideas, but turning those ideas into functional software can be time consuming, expensive and seem out of reach. Brainwave2Binaries specializes in helping small businesses and individuals take their idea from the back of a napkin to the desktop.</p>
    <p>Already have software and need to make improvements? We can help there, too. We've worked with numerous entrepreneurs and companies wanting to update their current software, whether it is making small bug fixes or adding new functionality.</p>
  </div>
</section>

<section class="abs team">
  <svg class="abs arrow" style="left:27px" width="10" height="64"><polyline points="9,1 1,32 9,63" fill="none" stroke="#9aa0a6" stroke-width="1"/></svg>
  <svg class="abs arrow" style="left:769px" width="10" height="64"><polyline points="1,1 9,32 1,63" fill="none" stroke="#9aa0a6" stroke-width="1"/></svg>

  <div class="abs card" style="left:58px">
    <div class="band" style="background:var(--band-dark)"></div>
    <div class="avatar" role="img" aria-label="Team member portrait"></div>
    <h3>Jhon Smith</h3><div class="role">Technical Guy</div>
    <div class="bio">Already have software and need to make improvements? We can help entrepreneurs &amp; companies</div>
    <div class="divider"></div>
    <svg width="120" height="24" role="img" aria-label="Social links"><g fill="none" stroke="#ccd0d4"><circle cx="12" cy="12" r="10"/><circle cx="35" cy="12" r="10"/><circle cx="82" cy="12" r="10"/><circle cx="105" cy="12" r="10"/></g><circle cx="58" cy="12" r="10" fill="var(--sky)"/></svg>
  </div>
  <div class="abs card" style="left:234px">
    <div class="band" style="background:var(--sky-soft)"></div>
    <div class="avatar" role="img" aria-label="Team member portrait"></div>
    <h3>Jhon Smith</h3><div class="role">Business Girl</div>
    <div class="bio">Already have software and need to make improvements? We can help entrepreneurs &amp; companies</div>
    <div class="divider"></div>
    <svg width="120" height="24" role="img" aria-label="Social links"><g fill="none" stroke="#ccd0d4"><circle cx="12" cy="12" r="10"/><circle cx="35" cy="12" r="10"/><circle cx="82" cy="12" r="10"/><circle cx="105" cy="12" r="10"/></g><circle cx="58" cy="12" r="10" fill="var(--sky)"/></svg>
  </div>
  <div class="abs card" style="left:409px">
    <div class="band" style="background:var(--band-dark)"></div>
    <div class="avatar" role="img" aria-label="Team member portrait"></div>
    <h3>Jhon Smith</h3><div class="role">Technical Guy</div>
    <div class="bio">Already have software and need to make improvements? We can help entrepreneurs &amp; companies</div>
    <div class="divider"></div>
    <svg width="120" height="24" role="img" aria-label="Social links"><g fill="none" stroke="#ccd0d4"><circle cx="12" cy="12" r="10"/><circle cx="35" cy="12" r="10"/><circle cx="82" cy="12" r="10"/><circle cx="105" cy="12" r="10"/></g><circle cx="58" cy="12" r="10" fill="var(--sky)"/></svg>
  </div>
  <div class="abs card" style="left:585px">
    <div class="band" style="background:var(--sky-soft)"></div>
    <div class="avatar" role="img" aria-label="Team member portrait"></div>
    <h3>Jhon Smith</h3><div class="role">Business Girl</div>
    <div class="bio">Already have software and need to make improvements? We can help entrepreneurs &amp; companies</div>
    <div class="divider"></div>
    <svg width="120" height="24" role="img" aria-label="Social links"><g fill="none" stroke="#ccd0d4"><circle cx="12" cy="12" r="10"/><circle cx="35" cy="12" r="10"/><circle cx="82" cy="12" r="10"/><circle cx="105" cy="12" r="10"/></g><circle cx="58" cy="12" r="10" fill="var(--sky)"/></svg>
  </div>
</section>

<section class="abs contact">
  <h2>CONTACT <span>US</span></h2>
  <p class="lead">We write your software with your regular feedback to ensure the deliverable exceeds your expectations. We deliver and support</p>

  <div class="field" style="left:58px;top:90px;width:162px;height:24px">First Name :</div>
  <div class="field" style="left:226px;top:90px;width:162px;height:24px">Last Name :</div>
  <div class="field" style="left:58px;top:120px;width:162px;height:24px">Phone :</div>
  <div class="field" style="left:226px;top:120px;width:162px;height:24px">Email :</div>
  <div class="field" style="left:58px;top:149px;width:330px;height:80px">Message :</div>
  <div class="submit">SUBMIT</div>

  <p class="abs info-lead">As a small business ourselves, we understand the need to be flexible, efficient and cost-conscious. We can help with all stages of software design from creating simple prototypes to full-blown production systems.</p>

  <div class="abs label-sm" style="left:419px;top:150px">Address</div>
  <div class="abs info" style="left:418px;top:165px"># 2547 Lorem Ipsum Dummy<br>Lorem Ipsum Dummy</div>

  <div class="abs label-lg" style="left:588px;top:146px">EMAIL ADDRESS</div>
  <div class="abs info" style="left:587px;top:165px">General : info@brainwave2binaries-example.com<br>Office :contact@b2b-office-example.com</div>

  <div class="abs label-lg" style="left:419px;top:223px">PHONE</div>
  <div class="abs info" style="left:418px;top:243px">Mobile : (555) 014-2290</div>

  <div class="abs label-lg" style="left:588px;top:211px">FOLLOW US</div>
  <svg class="abs" style="left:582px;top:233px" width="145" height="28" role="img" aria-label="Social media links"><g fill="none" stroke="#a8adb3" stroke-width="1"><circle cx="14" cy="14" r="12"/><circle cx="43" cy="14" r="12"/><circle cx="71" cy="14" r="12"/><circle cx="100" cy="14" r="12"/><circle cx="129" cy="14" r="12"/></g></svg>
</section>

<footer class="abs site-footer">© Copyright 2017.Brainwave2Binaries .All Rights Reserved</footer>

</body>
</html>
```